Redesign Digital Lending Mobile App - Android/ Flutter

Want to re-theme an existing Digital Lending Mobile app to simplify customer journeys, as well as uplift the UI.

Most users will have small screen phones so the design needs to take that into consideration while also adapting to those with larger devices, like admins with Tablets.

Have already laid out customer journeys on Figma with guidance on how the flow of the app should be. https://www.plandeck.example/board/q4tRw8KzPmYx2LbNvcHsaT/KovaPay?view-id=3-5120&k=Zu8pRtQwLmNcXbYa-2

Video capture of current app: https://vault.trelmora.example/clip/d/7Hq2WmRtLp9XzKcVbNa4YsDfGe8JuQo3/view
https://vault.trelmora.example/clip/d/4Pn8ZxCvBq1MwLtRyHs6KdJgFa2UeXi9/view

The documented views for Web are also here https://docs.quenlaro.example/open?id=3A8C2D4F6B1E9077!kb2d58e71403a4c6e8f2a91d04b7c3e68&resid=3A8C2D4F6B1E9077!kb2d58e71403a4c6e8f2a91d04b7c3e68&cid=3a8c2d4f6b1e9077&ithint=file%2Cdocx&redeem=bXhZc2RrcVp0TmxhUGVvV2lGcnVHc0JtWWpLdlFhWHpOcHRMZUR3U2JjUmZUeUFnSGxNb1ZpRXVKd0NrRHNYcVBuWmFNYmd5TGVr&migratedtospo=true&wdo=2
Updates

Target Market(s)

Kenya, Tanzania, Uganda - Africa

Industry/Entity Type

Fintech

Requirements
Must have
• Responsive for diff screens, esp. in context of smaller screen smartphone
Nice to have
• Thematic components to ensure new views can easily be adapted to these themse

```html
<!DOCTYPE html>
<html lang="en">
<head>
<meta charset="utf-8">
<title>KovaPay – Lending App Screens</title>
<link rel="stylesheet" href="https://fonts.googleapis.com/css2?family=Montserrat:wght@400;500;600;700&family=Roboto:wght@400&display=swap">
<style>
:root{
  --canvas:#f1f1f1;
  --white:#ffffff;
  --brand:#3478c6;
  --brand-dark:#1e3fae;
  --poly-light:#2aa8ec;
  --poly-mid:#1673dd;
  --poly-deep:#0c1fa0;
  --ink:#111111;
  --muted:#6f6f6f;
  --line:#d4d4d4;
  --danger:#e02424;
  --kb-bg:#1b1b1b;
  --kb-key:#4a4a4a;
  --kb-key-dark:#333333;
  --drawer-shade:#ececec;
}
*{box-sizing:border-box;margin:0;padding:0}
html,body{width:961px;height:1200px;overflow:hidden;background:var(--canvas)}
body{position:relative;font-family:"Montserrat",Arial,sans-serif;color:var(--ink)}
.screen{position:absolute;width:208px;height:454px;background:var(--white);border-radius:18px;overflow:hidden}
.screen--splash{left:105px;top:111px}
.screen--login{left:376px;top:111px}
.screen--pin{left:646px;top:111px}
.screen--home{left:105px;top:630px}
.screen--drawer{left:376px;top:630px}
.backdrop{position:absolute;left:0;top:0;width:208px;height:454px}
.abs{position:absolute}
.center-x{left:0;right:0;text-align:center}

/* splash */
.brand-mark{position:absolute;left:0;right:0;top:196px;display:flex;flex-direction:column;align-items:center;gap:8px}
.brand-dot{width:30px;height:30px;border-radius:50%;background:var(--brand)}
.brand-name{font-size:19px;font-weight:700;color:var(--brand);letter-spacing:.3px}

/* forms */
.title{font-size:12px;font-weight:700;color:var(--brand)}
.label{font-size:7px;font-weight:500;left:14px}
.field{left:14px;width:179px;height:24px;border:1px solid var(--line);border-radius:3px;font-size:6.5px;color:#a9a9a9;padding:0 10px;display:flex;align-items:center}
.link{color:var(--brand)}
.btn{left:14px;width:179px;height:23px;border-radius:3px;background:var(--brand);color:var(--white);font-size:8.5px;display:flex;align-items:center;justify-content:center}
.btn--ghost{background:var(--white);border:1px solid var(--line);color:#555;font-weight:500}
.divider-or{left:14px;width:179px;display:flex;align-items:center;gap:4px;font-size:7.5px}
.divider-or::before,.divider-or::after{content:"";flex:1;height:1px;background:#9a9a9a}
.small{font-size:6.8px;font-weight:500}
.checkbox{width:10px;height:10px;border:1px solid var(--line);border-radius:2px;left:14px}

/* pin */
.pin-row{left:14px;width:179px;display:flex;justify-content:space-between}
.pin-box{width:21px;height:25px;border:1px solid var(--line);border-radius:3px;font-size:16px;display:flex;align-items:center;justify-content:center;font-weight:500}
.keyboard{position:absolute;left:0;top:279px;width:208px;height:175px;background:var(--kb-bg);font-family:"Roboto",Arial,sans-serif;color:#eee}
.kb-chip{position:absolute;left:75px;top:4px;width:58px;height:18px;border-radius:9px;background:#3b3b3b;font-size:7.5px;color:#bbb;display:flex;align-items:center;justify-content:center;gap:4px}
.kb-chip i{width:8px;height:8px;border:1px solid #4a90e2;border-radius:2px;display:block}
.kb-row{position:absolute;left:3px;width:202px;display:flex;gap:2.2px}
.key{flex:1;height:23px;border-radius:4px;background:var(--kb-key);font-size:11px;display:flex;align-items:center;justify-content:center}
.key--dark{background:var(--kb-key-dark);font-size:8px}
.kb-chevron{position:absolute;left:16px;top:156px;width:5px;height:5px;border-right:1px solid #ccc;border-bottom:1px solid #ccc;transform:rotate(45deg)}

/* profile */
.avatar{position:absolute;border-radius:50%;background:linear-gradient(160deg,#6a7592,#3f4a66);border:2.5px solid #0a0a0a}
.level-badge{position:absolute;width:36px;height:36px;border-radius:50%;background:var(--brand);color:var(--white);font-size:6.8px;font-weight:600;display:flex;align-items:center;justify-content:center}
.greeting{left:93px;top:67px;font-size:13.4px;font-weight:700}
.greeting-name{left:93px;top:87px;font-size:9.5px;font-weight:500;color:var(--muted)}
.section-head{left:14px;width:179px;top:171px;display:flex;justify-content:space-between;align-items:baseline}
.section-head strong{font-size:6.8px;font-weight:700}
.section-head span{font-size:6px;color:var(--brand);font-weight:500}
.plan-card{position:absolute;left:14px;width:179px;height:87px;background:var(--white);border:1px solid var(--line);border-radius:6px}
.plan-tag{position:absolute;top:4px;height:13px;border-radius:7px;background:#f2f2f2;border:1px solid #e3e3e3;font-size:5.2px;display:flex;align-items:center;justify-content:center}
.plan-tag--status{left:3px;width:48px;color:var(--danger)}
.plan-tag--amount{right:3px;width:48px}
.plan-pill{position:absolute;left:56px;top:-5px;width:66px;height:18px;border-radius:9px;background:var(--brand);color:var(--white);font-size:7px;display:flex;align-items:center;justify-content:center;box-shadow:0 0 0 3px var(--white)}
.plan-text{position:absolute;left:7px;right:7px;top:29px;font-size:5.6px;line-height:6.8px;color:var(--muted)}
.bottom-nav{position:absolute;left:14px;top:411px;width:179px;height:28px;background:var(--white);border-radius:4px;display:flex;align-items:center;padding:0 3px;font-size:6.5px;font-weight:600}
.nav-item{flex:1;display:flex;flex-direction:column;align-items:center;gap:1px}
.nav-item--active{flex:0 0 62px;height:22px;border-radius:4px;background:var(--brand);color:var(--white);flex-direction:row;justify-content:center;gap:5px;font-weight:500}

/* drawer */
.drawer-shade{position:absolute;left:157px;top:0;width:51px;height:454px;background:var(--drawer-shade)}
.profile-name{left:0;width:157px;text-align:center;top:108px;font-size:10.5px;font-weight:700}
.profile-meta{left:0;width:157px;text-align:center;font-size:6.5px;font-weight:500;line-height:8px}
.rule{left:14px;width:127px;height:1px;background:#444}
.menu-item{left:14px;display:flex;align-items:center;gap:7px;font-size:8.2px;font-weight:600}
.menu-item svg{width:11px;height:11px}
</style>
</head>
<body>

<!-- Splash -->
<section class="screen screen--splash" aria-label="Splash screen">
  <svg class="backdrop" viewBox="0 0 208 454" role="img" aria-label="Blue low-poly backdrop">
    <defs>
      <linearGradient id="polyTop" x1="0" y1="1" x2="1" y2="0"><stop offset="0" stop-color="var(--poly-deep)"/><stop offset=".55" stop-color="var(--poly-mid)"/><stop offset="1" stop-color="var(--poly-light)"/></linearGradient>
      <linearGradient id="polyBottom" x1="0" y1="1" x2="1" y2="0"><stop offset="0" stop-color="var(--poly-light)"/><stop offset=".5" stop-color="var(--poly-mid)"/><stop offset="1" stop-color="var(--poly-deep)"/></linearGradient>
    </defs>
    <polygon points="0,0 208,0 208,14 182,22 160,46 128,68 102,92 60,93 0,108" fill="url(#polyTop)"/>
    <polygon points="208,345 208,454 0,454 28,418 52,410 90,378 146,358 160,356 192,348" fill="url(#polyBottom)"/>
  </svg>
  <div class="brand-mark"><span class="brand-dot"></span><span class="brand-name">KovaPay</span></div>
</section>

<!-- Login -->
<section class="screen screen--login" aria-label="Log in or register">
  <svg class="backdrop" viewBox="0 0 208 454" role="img" aria-label="Blue low-poly backdrop">
    <polygon points="0,0 208,0 208,14 182,22 160,46 128,68 102,92 60,93 0,108" fill="url(#polyTop)"/>
    <polygon points="208,345 208,454 0,454 28,418 52,410 90,378 146,358 160,356 192,348" fill="url(#polyBottom)"/>
  </svg>
  <h1 class="abs title center-x" style="top:111px">Log In/Register</h1>
  <div class="abs label" style="top:140px">UserName or Email:</div>
  <div class="abs field" style="top:151px">Enter UserName or Email</div>
  <div class="abs label" style="top:181px">Password:</div>
  <div class="abs field" style="top:192px">Enter Password</div>
  <div class="abs small link" style="left:14px;top:221px">Forgot Password?</div>
  <div class="abs btn" style="top:233px">Login</div>
  <div class="abs divider-or" style="top:259px">or</div>
  <div class="abs btn btn--ghost" style="top:273px">Nexlo</div>
  <div class="abs small" style="left:14px;top:303px">Not have account: <span class="link">Register Now</span></div>
  <div class="abs checkbox" style="top:326px"></div>
  <div class="abs small" style="left:28px;top:324px;width:168px;line-height:8px">I'm agree to the <span class="link">Term of Service</span> and the <span class="link">Privacy Policy.</span></div>
</section>

<!-- PIN -->
<section class="screen screen--pin" aria-label="Enter PIN">
  <svg class="backdrop" viewBox="0 0 208 454" role="img" aria-label="Blue low-poly backdrop">
    <polygon points="0,0 208,0 208,14 182,22 160,46 128,68 102,92 60,93 0,108" fill="url(#polyTop)"/>
  </svg>
  <div class="abs center-x" style="top:162px;font-size:8.4px;font-weight:500">Enter Your Pin</div>
  <div class="abs pin-row" style="top:178px">
    <span class="pin-box">7</span><span class="pin-box">9</span><span class="pin-box">7</span><span class="pin-box">0</span><span class="pin-box">9</span><span class="pin-box">3</span>
  </div>
  <div class="abs btn" style="top:213px">Submit</div>
  <div class="keyboard" aria-label="On-screen keyboard">
    <div class="kb-chip"><i></i>797093</div>
    <div class="kb-row" style="top:30px"><span class="key">q</span><span class="key">w</span><span class="key">e</span><span class="key">r</span><span class="key">t</span><span class="key">y</span><span class="key">u</span><span class="key">i</span><span class="key">o</span><span class="key">p</span></div>
    <div class="kb-row" style="top:61px;padding:0 10px"><span class="key">a</span><span class="key">s</span><span class="key">d</span><span class="key">f</span><span class="key">g</span><span class="key">h</span><span class="key">j</span><span class="key">k</span><span class="key">l</span></div>
    <div class="kb-row" style="top:92px"><span class="key key--dark" style="flex:1.5">⇧</span><span class="key">z</span><span class="key">x</span><span class="key">c</span><span class="key">v</span><span class="key">b</span><span class="key">n</span><span class="key">m</span><span class="key key--dark" style="flex:1.5">⌫</span></div>
    <div class="kb-row" style="top:123px"><span class="key key--dark" style="flex:1.6">?123</span><span class="key key--dark">☺</span><span class="key key--dark">,</span><span class="key" style="flex:4.4;font-size:7.5px">English (USA)</span><span class="key key--dark">.</span><span class="key key--dark" style="flex:1.5;color:#4a90e2">⌕</span></div>
    <span class="kb-chevron"></span>
  </div>
</section>

<!-- Home -->
<section class="screen screen--home" aria-label="Home">
  <svg class="backdrop" viewBox="0 0 208 454" role="img" aria-label="Blue low-poly backdrop">
    <polygon points="0,0 208,0 208,12 186,20 160,44 130,62 96,84 70,84 0,108" fill="url(#polyTop)"/>
    <polygon points="208,343 208,454 0,454 22,428 40,420 80,414 92,400 110,395 150,372 180,350" fill="url(#polyBottom)"/>
  </svg>
  <div class="avatar" role="img" aria-label="User profile photo" style="left:15px;top:47px;width:56px;height:56px"></div>
  <div class="level-badge" style="left:38px;top:84px">Level: 2</div>
  <div class="abs greeting">Good Morning</div>
  <div class="abs greeting-name">John Doe</div>
  <div class="abs section-head"><strong>Loan Eligibility Plans</strong><span>View all plans</span></div>
  <article class="plan-card" style="top:200px">
    <span class="plan-tag plan-tag--status">Not Eligible</span>
    <span class="plan-pill">Plan 1</span>
    <span class="plan-tag plan-tag--amount">Upto $10000</span>
    <p class="plan-text">Short-term working capital for small traders with steady mobile money records. Repay weekly over twelve weeks with a flat service fee. Requires an active account for at least six months and a clean repayment history on past loans. Group members may apply together and share one guarantee across the whole group. <span class="link">read more</span></p>
  </article>
  <article class="plan-card" style="top:308px">
    <span class="plan-tag plan-tag--status">Not Eligible</span>
    <span class="plan-pill">Plan 2</span>
    <span class="plan-tag plan-tag--amount">Upto $10000</span>
    <p class="plan-text">Asset financing for farmers and boda riders buying tools, seed or motorbikes. Pay back monthly over up to one year at a fixed rate. Needs a registered group, a guarantor from that group and a history of regular savings deposits into the account. Top ups open after half the term. <span class="link">read more</span></p>
  </article>
  <nav class="bottom-nav">
    <span class="nav-item nav-item--active"><svg width="11" height="10" viewBox="0 0 12 11" fill="none" stroke="#fff" stroke-width="1"><path d="M1 5 6 1l5 4v5.5H1z"/></svg>Home</span>
    <span class="nav-item"><svg width="9" height="11" viewBox="0 0 9 11" fill="none" stroke="#111" stroke-width=".8"><path d="M4.5 1C6 3 8 5 8 7.5A3.5 3.5 0 0 1 1 7.5C1 5.5 3 4 4.5 1z"/></svg>Tutorials</span>
    <span class="nav-item"><svg width="10" height="10" viewBox="0 0 10 10" fill="none" stroke="#111" stroke-width=".9"><circle cx="5" cy="5" r="1.6"/><circle cx="5" cy="5" r="3.8" stroke-dasharray="2 1"/></svg>Setting</span>
  </nav>
</section>

<!-- Drawer -->
<section class="screen screen--drawer" aria-label="Navigation drawer">
  <span class="drawer-shade"></span>
  <svg class="backdrop" viewBox="0 0 208 454" role="img" aria-label="Blue low-poly backdrop" style="width:157px" preserveAspectRatio="none">
    <polygon points="0,0 157,0 157,10 140,16 125,32 110,40 90,50 56,58 0,82" fill="url(#polyTop)" transform="scale(1.325,1)"/>
    <polygon points="157,372 157,454 0,454 14,440 40,410 60,406 90,380 116,368 140,385" fill="url(#polyBottom)" transform="scale(1.325,1)"/>
  </svg>
  <div class="avatar" role="img" aria-label="User profile photo" style="left:48px;top:24px;width:61px;height:61px"></div>
  <div class="level-badge" style="left:72px;top:65px">Level: 2</div>
  <div class="abs profile-name">John Doe</div>
  <div class="abs profile-meta" style="top:120px">Branch<br>Organization</div>
  <div class="abs rule" style="top:139px"></div>
  <div class="abs menu-item" style="top:158px"><svg viewBox="0 0 11 11" fill="none" stroke="#111" stroke-width=".8"><rect x=".5" y=".5" width="4" height="5"/><rect x="6.5" y=".5" width="4" height="3"/><rect x=".5" y="7.5" width="4" height="3"/><rect x="6.5" y="5.5" width="4" height="5"/></svg>Dashboard</div>
  <div class="abs menu-item" style="top:197px"><svg viewBox="0 0 11 11" fill="none" stroke="#111" stroke-width=".8"><circle cx="5.5" cy="3.2" r="2.5"/><path d="M1 10.5a4.5 4.5 0 0 1 9 0z"/></svg>Clients</div>
  <div class="abs menu-item" style="top:236px"><svg viewBox="0 0 11 11" fill="none" stroke="#111" stroke-width=".7"><circle cx="5.5" cy="4" r="1.6"/><circle cx="2.3" cy="4.8" r="1.2"/><circle cx="8.7" cy="4.8" r="1.2"/><path d="M2.8 9a2.7 2.7 0 0 1 5.4 0M.5 9a1.8 1.8 0 0 1 2.4-1.8M10.5 9a1.8 1.8 0 0 0-2.4-1.8"/></svg>Groups</div>
  <div class="abs menu-item" style="top:275px"><svg viewBox="0 0 11 11" fill="none" stroke="#111" stroke-width=".7"><rect x="1" y="2" width="5" height="8.5"/><rect x="6" y="4.5" width="4" height="6"/><path d="M2.5 4h2M2.5 6h2M2.5 8h2M7.3 6.5h1.4M7.3 8.5h1.4"/></svg>Centers</div>
  <div class="abs menu-item" style="top:314px"><svg viewBox="0 0 11 11" fill="none" stroke="#111" stroke-width=".8"><circle cx="5.5" cy="5.5" r="5"/><circle cx="5.5" cy="4.2" r="1.8"/><path d="M2.3 9a3.6 3.6 0 0 1 6.4 0"/></svg>Profile</div>
  <div class="abs rule" style="top:370px"></div>
  <div class="abs menu-item" style="top:379px"><svg viewBox="0 0 11 11" fill="none" stroke="#111" stroke-width=".8"><path d="M4.5 1H1v9h3.5M4 5.5h6.5M8.5 3.5l2 2-2 2"/></svg>Log out</div>
</section>

</body>
</html>
```